Womens Personal Training studio needs new year flyers

I need a double sided A5 flyer to attract Women / Mothers to my fitness business, Radiant Core Studio, in the new year.

My business colour is teal, I am located in Oakvale QLD Aus

Exclusive studio training for women. At Radiant Core Studio we don't make New years resolutions, we Empower you to make the changes for life!

examples of pain Q's: Do you feel guilty about wanting to do something for yourself? Do you worry about what exercises are safe post baby? Are you struggling to regain control of your body and your life?

Would you like to love yourself and your body as much as you lvoe your baby?

I work with women to apporpriately and progressivley rebuild their bodies post preganany. As the Leading specialist in Pre and Post Natal Rehabilitation and Fitness in Durnford, Marnie knows what it takes to find the right balance. With a vision of Empowering this generation to inspire the next, Marnie teaches skills for LIFE so you can lead your family to a Healthier, Fitter and Stronger future! Using a fusion of Pilates, Strength Conditioning and Cardio Marnie customises a plan for each individual. Your free consultation is waiting call now and learn the first steps to making the change Valued at $147 Don’t Miss out!! Marnie 0438 270 614

Quote to go with image "Marnie doesn't just help you achieve your weight loss goals she works with you to make sure you are 'Radiant Core Studio'." Tessa Brook July 2013

Target Market(s)

Women / Mothers

Industry/Entity Type

Training

Requirements
Must have
• call to action
contact details
Marnie Clarke
0438 270 614
marnie@radiantcorestudio.net.au
www.radiantcorestudio.net.au

```html
<!DOCTYPE html>
<html lang="en">
<head>
<meta charset="utf-8">
<title>Radiant Core Studio – Flyer Front</title>
<link href="https://fonts.googleapis.com/css2?family=Lato:wght@400;700;900&family=IM+Fell+English:ital@0;1&display=swap" rel="stylesheet">
<style>
  :root{
    --ink:#231f20;
    --teal:#1a8f98;
    --teal-deep:#127a83;
    --teal-soft:#bfe3e6;
    --pink:#e5197f;
    --white:#ffffff;
    --text:#2b2b2b;
    --photo-a:#1d6c86;
    --photo-b:#2b8ea6;
  }
  *{margin:0;padding:0;box-sizing:border-box}
  html,body{width:885px;height:1200px;overflow:hidden;background:#fff}
  body{font-family:'Lato',sans-serif;color:var(--text)}
  .flyer{position:relative;width:885px;height:1200px;overflow:hidden;
    background:linear-gradient(180deg,#fff 30%,#eef8f9 55%,#fff 75%)}
  .flyer-shapes{position:absolute;inset:0}
  .photo{position:absolute;background:linear-gradient(180deg,var(--photo-a),var(--photo-b))}
  .photo-label{position:absolute;left:0;right:0;bottom:0;height:52px;background:var(--teal);
    color:#fff;font-weight:700;font-size:28px;display:flex;align-items:center;justify-content:center;letter-spacing:.5px}
  .photo-before{left:63px;top:49px;width:196px;height:279px}
  .photo-after{left:267px;top:49px;width:196px;height:279px}
  .testimonial{position:absolute;left:480px;top:56px;width:370px;color:#fff;
    font-family:'IM Fell English',serif;font-size:19px;line-height:33px}
  .testimonial-author{position:absolute;left:640px;top:188px;color:var(--teal);font-weight:700;font-size:20px}
  .brand{position:absolute;left:68px;top:350px;display:flex;align-items:center;gap:16px;
    color:var(--teal);font-weight:700;font-size:46px}
  .brand-dot{width:30px;height:30px;border-radius:50%;background:var(--teal)}
  .headline{position:absolute;left:316px;top:432px;width:500px;font-weight:700;font-size:22px;line-height:29px;color:var(--ink)}
  .services{position:absolute;left:276px;top:0;list-style:none;width:500px}
  .services li{position:absolute;left:0;width:500px;padding-left:40px;font-size:18px;line-height:24px;color:var(--text);white-space:nowrap}
  .services li::before{content:"";position:absolute;left:0;top:7px;width:11px;height:11px;background:var(--pink)}
  .cta-box{position:absolute;left:21px;top:528px;width:183px;height:323px;background:var(--ink);
    color:#fff;font-weight:700;font-size:22px;line-height:28px;padding:26px 0 0 14px}
  .cta-box .cta-title{font-weight:900;font-size:23px;padding-left:8px;margin-bottom:10px}
  .cta-box .accent{color:var(--pink)}
  .trainer-photo{position:absolute;left:700px;top:760px;width:185px;height:440px;
    background:linear-gradient(180deg,#d9b9a3,#c39d86 45%,#2a2a2a 70%,#1c1c1c);
    clip-path:polygon(75px 0,185px 0,185px 100%,0 100%,0 160px,75px 140px)}
  .consult{position:absolute;left:50px;top:1045px;color:#fff}
  .consult-title{color:var(--pink);font-weight:700;font-size:23px}
  .consult-phone{font-weight:700;font-size:36px;margin-top:8px}
  .consult-email{font-weight:700;font-size:20px;margin-top:4px}
  .help-label{position:absolute;left:476px;top:1042px;color:#fff;font-weight:700;font-size:16px}
  .help-bar{position:absolute;left:434px;top:1068px;width:451px;height:58px;background:var(--teal);
    border-radius:14px 0 0 14px}
  .help-name{position:absolute;left:100px;top:8px;color:#fff;font-weight:700;font-size:20px}
  .help-role{position:absolute;left:166px;top:34px;color:#fff;font-weight:700;font-size:13px}
</style>
</head>
<body>
<main class="flyer">
  <svg class="flyer-shapes" width="885" height="1200" viewBox="0 0 885 1200" aria-hidden="true">
    <path d="M0 560 C250 480 520 720 885 600 L885 680 C560 790 280 560 0 660Z" fill="var(--teal-soft)" opacity=".45"/>
    <path d="M0 760 C300 650 600 900 885 780 L885 830 C600 950 300 720 0 830Z" fill="var(--teal-soft)" opacity=".55"/>
    <path d="M0 0 H885 V220 L641 285 L0 136Z" fill="var(--ink)"/>
    <path d="M0 136 L641 285 L885 220 V236 L641 303 L0 154Z" fill="var(--teal)"/>
    <path d="M0 1018 L257 901 L885 1044 V1200 H0Z" fill="var(--teal)"/>
    <path d="M0 1036 L257 920 L885 1062 V1200 H0Z" fill="var(--ink)"/>
  </svg>

  <div class="photo photo-before" role="img" aria-label="Side-view photo of a client before training">
    <div class="photo-label">BEFORE</div>
  </div>
  <div class="photo photo-after" role="img" aria-label="Side-view photo of the same client after training">
    <div class="photo-label">AFTER</div>
  </div>

  <blockquote class="testimonial">"Marnie doesn't just help you achieve your weight loss goals she works with you to make sure you are 'Radiant Core Studio'."</blockquote>
  <p class="testimonial-author">Tessa Brook July 2013</p>

  <div class="brand"><span>Radiant Core Studio</span><span class="brand-dot"></span></div>

  <h1 class="headline">I work with women to apporpriately and progres-sivley rebuild their bodies post preganany</h1>

  <ul class="services">
    <li style="top:549px">Pre and Post Natal Rehabilitation and Fitness in Durnford</li>
    <li style="top:597px">Marnie knows what it takes to find the right balance.<br>With a vision of Empowering this generation to inspire<br>the next</li>
    <li style="top:698px">Marnie teaches skills for LIFE so you can lead your<br>family to a Healthier</li>
    <li style="top:771px">Fitter and Stronger future! Using a fusion of<br>Pilates</li>
    <li style="top:846px">Strength Conditioning and Cardio Marnie customises a<br>plan for each individual.</li>
  </ul>

  <aside class="cta-box">
    <p class="cta-title">CALL NOW<br>&amp; LEARN</p>
    <p>the first steps to making the change Valued at <span class="accent">$147 Don't Miss out!!</span><br>Marnie<br><span class="accent">0438 270 614</span></p>
  </aside>

  <div class="trainer-photo" role="img" aria-label="Photo of a smiling female trainer holding a clipboard"></div>

  <section class="consult">
    <p class="consult-title">YOUR FREE CONSULTATION</p>
    <p class="consult-phone">0438 270 614</p>
    <p class="consult-email">info@radiantcorestudio.net.au</p>
  </section>

  <p class="help-label">YOU need help?</p>
  <div class="help-bar">
    <span class="help-name">Jordan Hale</span>
    <span class="help-role">gym instructor</span>
  </div>
</main>
</body>
</html>
```